Commercial Office Fitout company needs a simple website

We need a website for our company Harbourline Fitouts (QLD) Pty Ltd. We are in the construction industry and we specialise in commercial office fitouts (partitions/glass/doors). Our company colours are black and silver. Please use our logo attached.
We only need an "about us" section, a "portfolio" section where we display some pictures of our work, and a "contact us" section. We would like our website to be simple, effective, professional and modern.

Industry/Entity Type

Construction

Number of Pages Required

1 page

```html
<!DOCTYPE html>
<html lang="en">
<head>
<meta charset="utf-8">
<title>Harbourline Fitouts (QLD) Pty Ltd</title>
<link href="https://fonts.googleapis.com/css2?family=Montserrat:wght@400;500;600;700&family=Oswald:wght@300;400&family=Lato:wght@400&display=swap" rel="stylesheet">
<style>
:root{
  --black:#060606;
  --charcoal:#141210;
  --brown:#3a2f2a;
  --brown-dark:#2a211d;
  --silver:#e9e9e9;
  --floor-top:#eceded;
  --floor-bottom:#fbfbfb;
  --text:#2b2b2b;
  --muted:#555;
  --white:#fff;
  --frame:#8a7a6a;
}
*{box-sizing:border-box;margin:0;padding:0}
html,body{width:756px;height:1200px;overflow:hidden}
body{position:relative;background:var(--floor-bottom);font-family:"Montserrat",sans-serif;color:var(--text)}
.abs{position:absolute}

.site-header{left:0;top:0;width:756px;height:110px;background:linear-gradient(#151515,var(--black));border-bottom:1px solid #555}
.tollfree{left:62px;top:26px;color:var(--white)}
.tollfree .label{font-size:11px;display:flex;align-items:center;gap:5px}
.tollfree .number{font-size:17px;margin-top:2px}
.brand-badge{left:298px;top:-82px;width:160px;height:164px;border-radius:50%;background:var(--silver);border:6px solid #9a9a9a;display:flex;flex-direction:column;align-items:center;justify-content:flex-end;padding-bottom:18px}
.brand-name{font-size:11px;font-weight:700;color:#1b1b1b;letter-spacing:.5px;line-height:1.25;text-align:center}
.brand-name small{display:block;font-size:7px}
.social{right:62px;top:30px;display:flex;gap:8px}
.social span{width:25px;height:25px;border-radius:50%;background:#bbb;border:3px solid #6d6d6d}
.main-nav{left:0;top:89px;width:756px;display:flex;justify-content:center;gap:20px;font-size:10px;color:var(--white)}
.main-nav .sep{color:#666}

.hero-band{left:0;top:111px;width:756px;height:272px;background:linear-gradient(90deg,var(--brown-dark),var(--brown) 20%,var(--brown) 80%,var(--brown-dark))}
.floor{left:0;top:383px;width:756px;height:250px;background:linear-gradient(var(--floor-top),var(--floor-bottom))}
.hero{left:98px;top:132px;width:559px;height:283px;border:3px solid #cfcfcf;box-shadow:0 2px 6px rgba(0,0,0,.4);background:linear-gradient(160deg,#f2f2f0,#d8d8d4 55%,#b9b8b2)}
.hero h1{position:absolute;left:42px;top:208px;font-family:"Oswald",sans-serif;font-weight:400;font-size:26px;line-height:1.15;color:#222}
.hero h1 span{display:block;font-weight:300;font-size:22px;margin-top:2px}

.section-title{position:absolute;left:0;width:756px;text-align:center;font-size:20px;font-weight:400;color:#1c1c1c}
.divider{position:absolute;left:312px;width:132px;height:1px;background:#d3d3d3}
.divider::after{content:"";position:absolute;left:61px;top:-5px;width:10px;height:10px;border-radius:50%;background:#333;border:2px solid #ddd}
.about-text{left:84px;top:521px;width:588px;font-family:"Lato",sans-serif;font-size:7.6px;line-height:14px;text-align:center;color:#222}
.more{left:0;width:756px;text-align:center;font-size:8.5px;color:#333}

.portfolio{left:62px;top:627px;width:631px;height:237px;background:linear-gradient(var(--white),#f6f6f6)}
.work{top:703px;width:188px;height:115px;border:2px solid var(--frame);background:linear-gradient(150deg,#d7d7d0,#8a8f90)}
.arrow{top:748px;width:18px;height:18px;background:#ccc;display:flex;align-items:center;justify-content:center}

.contact{left:62px;top:864px;width:631px;height:248px;background:linear-gradient(#0a0908,#17130f)}
.contact .section-title{color:var(--white);width:631px}
.field{border:1px solid #555;background:#030303;color:#9a9a9a;font-size:7.5px;padding:6px;font-family:"Montserrat",sans-serif}
.submit{left:16px;top:203px;width:53px;height:21px;background:var(--white);color:#111;font-size:8px;font-weight:600;display:flex;align-items:center;justify-content:center}
.map{left:347px;top:85px;width:268px;height:140px;border:3px solid #5a5a5a;background:linear-gradient(135deg,#efe6c8,#e6dcb8 50%,#c9d9b0)}

.info-bar{left:0;top:1066px;width:756px;height:96px;background:linear-gradient(90deg,var(--brown-dark),#3b302b 50%,var(--brown-dark));z-index:-1}
.info-item{top:1123px;display:flex;gap:9px;color:var(--white)}
.info-item .ico{width:21px;height:21px;border-radius:50%;background:var(--white);display:flex;align-items:center;justify-content:center;margin-top:3px}
.info-item b{display:block;font-weight:400;font-size:9px;margin-bottom:3px}
.info-item p{font-family:"Lato",sans-serif;font-size:7.8px}
.copyright{left:0;top:1162px;width:756px;height:38px;background:var(--black);color:var(--white);font-size:8px;display:flex;align-items:center;justify-content:center;letter-spacing:.2px}
</style>
</head>
<body>
<header class="site-header abs">
  <div class="tollfree abs">
    <div class="label"><svg width="10" height="10" viewBox="0 0 24 24"><path fill="#fff" d="M6.6 10.8a15.1 15.1 0 0 0 6.6 6.6l2.2-2.2c.3-.3.7-.4 1-.2 1.1.4 2.3.6 3.6.6.6 0 1 .4 1 1V20c0 .6-.4 1-1 1C10.6 21 3 13.4 3 4c0-.6.4-1 1-1h3.5c.6 0 1 .4 1 1 0 1.3.2 2.5.6 3.6.1.3 0 .7-.2 1z"/></svg>Toll Us</div>
    <div class="number">800 45 7812</div>
  </div>
  <div class="brand-badge abs"><div class="brand-name">HARBOURLINE<small>FITOUTS (QLD) PTY LTD</small></div></div>
  <div class="social abs" aria-label="Social links"><span></span><span></span><span></span></div>
  <nav class="main-nav abs"><span class="sep">|</span><span>Home</span><span class="sep">|</span><span>About Us</span><span class="sep">|</span><span>Services</span><span class="sep">|</span><span>contact Us</span><span class="sep">|</span></nav>
</header>

<div class="hero-band abs"></div>
<div class="floor abs"></div>

<section class="hero abs" role="img" aria-label="Modern office fitout with glass partitions, leather armchairs and a glass coffee table">
  <h1>WE SPECIALISE IN<span>COMMERCIAL OFFICE FIT OUTS</span></h1>
</section>

<h2 class="section-title" style="top:454px">About Harbourline Fitouts</h2>
<div class="divider" style="top:496px"></div>
<p class="about-text abs">There are many variations of passages of Lorem Ipsum available, but the majority have suffered alteration in some form, by injected humour, or randomised words which don't look even slightly believable. If you are going to use a passage of Lorem Ipsum, you need to be sure there isn't anything embarrassing hidden in the middle of text. All the Lorem Ipsum generators on the Internet tend to repeat predefined chunks as necessary, making this the first true generator on the Internet. It uses a dictionary of over 200 Latin words, combined with a handful.</p>
<div class="more abs" style="top:589px">Read More »</div>

<section class="portfolio abs"></section>
<h2 class="section-title" style="top:645px">Our Portfolio</h2>
<div class="divider" style="top:679px"></div>
<div class="arrow abs" style="left:55px"><svg width="8" height="8" viewBox="0 0 8 8"><path d="M6 0L1 4l5 4" fill="none" stroke="#fff"/></svg></div>
<div class="work abs" role="img" aria-label="Aluminium framed glass shopfront entrance" style="left:78px"></div>
<div class="work abs" role="img" aria-label="Frameless glass retail entry doors" style="left:283px"></div>
<div class="work abs" role="img" aria-label="Timber framed glass office partition" style="left:489px"></div>
<div class="arrow abs" style="left:684px"><svg width="8" height="8" viewBox="0 0 8 8"><path d="M2 0l5 4-5 4" fill="none" stroke="#fff"/></svg></div>
<div class="more abs" style="top:831px">View All »</div>

<section class="contact abs">
  <h2 class="section-title" style="top:24px">Contact Us</h2>
  <div class="divider" style="top:58px;left:250px"></div>
  <div class="field abs" style="left:15px;top:87px;width:148px;height:22px">Name</div>
  <div class="field abs" style="left:174px;top:87px;width:148px;height:22px">Email</div>
  <div class="field abs" style="left:15px;top:117px;width:307px;height:22px">Name</div>
  <div class="field abs" style="left:15px;top:146px;width:307px;height:46px">Message</div>
  <div class="submit abs">SUBMIT</div>
  <div class="map abs" role="img" aria-label="Street map showing office location"></div>
</section>

<div class="info-bar abs"></div>
<div class="info-item abs" style="left:158px">
  <div class="ico"><svg width="10" height="11" viewBox="0 0 24 24"><path fill="#222" d="M12 2a7 7 0 0 0-7 7c0 5 7 13 7 13s7-8 7-13a7 7 0 0 0-7-7zm0 9.5A2.5 2.5 0 1 1 12 6a2.5 2.5 0 0 1 0 5.5z"/></svg></div>
  <div><b>Harbourline</b><p>274Lorem Ipsum is simply dummy text</p></div>
</div>
<div class="info-item abs" style="left:372px">
  <div class="ico"><svg width="10" height="10" viewBox="0 0 24 24"><path fill="#222" d="M6.6 10.8a15.1 15.1 0 0 0 6.6 6.6l2.2-2.2c.3-.3.7-.4 1-.2 1.1.4 2.3.6 3.6.6.6 0 1 .4 1 1V20c0 .6-.4 1-1 1C10.6 21 3 13.4 3 4c0-.6.4-1 1-1h3.5c.6 0 1 .4 1 1 0 1.3.2 2.5.6 3.6.1.3 0 .7-.2 1z"/></svg></div>
  <div><b>Call Us :</b><p>800 45 7812</p></div>
</div>
<div class="info-item abs" style="left:484px">
  <div class="ico"><svg width="10" height="8" viewBox="0 0 20 14"><rect width="20" height="14" rx="1" fill="#222"/><path d="M1 1l9 7 9-7" fill="none" stroke="#fff" stroke-width="1.5"/></svg></div>
  <div><b>Email Us :</b><p>info@harbourlinefitouts.com</p></div>
</div>
<footer class="copyright abs">COPYRIGHT © 2016 HARBOURLINE FITOUTS. ALL RIGHTS RESERVED.</footer>
</body>
</html>
```